Now Open Poster

We need a banner for our sports supplement and nutritional store, Harbor Nutrition.
We were hoping for some sort of creative word art piece.
I have drawn my own mock up just to give you all a very basic starting point. But you are free to go with whatever you feel will work best.
The primary objective is simply to explain a little about what the company does, and then direct traffic towards the store with an 'Open Arrow' pointing left.
Text words we have chosen are:
Protein
Creatine
Health
Fitness
Sports Science
Nutrition
Energy
Achievement
Amino Acids
Organic
Supplements
Performance
Testosterone Support
Vitamins
Growth
Diet
Happiness
Weight Loss
Strong
Natural
Vitality
Accomplished
Below the word art we want our logo (See attached options)
Then below the logo the phrase "Success Starts Here"
Dimensions of the poster are 140cm x 60cm.
Colours: Blues/Whites/Greys/Blacks (Lots of white space please)
Here are some cool pieces I found that had some interesting elements that I liked (I'd love to see a mash-up of styles with a street art feel to it. Something funky!):
http://www.moodgrove.example/pin/804417263190552871/
http://www.moodgrove.example/pin/615380924471208539/
http://www.moodgrove.example/pin/804417263192736155/
http://www.moodgrove.example/pin/804417263194418620/
http://www.moodgrove.example/pin/937162048856301742/
Thanks for reading, message me if you have any further questions!
- Tobias

```html
<!DOCTYPE html>
<html lang="en">
<head>
<meta charset="utf-8">
<title>Harbor Nutrition – Now Open Banner</title>
<link href="https://fonts.googleapis.com/css2?family=Antonio:wght@300;400;600;700&family=Orbitron:wght@700&family=PT+Sans:wght@700&family=Six+Caps&display=swap" rel="stylesheet">
<style>
  :root{
    --ink:#111111;
    --deep-teal:#1f5466;
    --slate-teal:#5a8b8b;
    --mist:#8ab3bb;
    --aqua:#6fc3c4;
    --lagoon:#3aa6ab;
    --sage:#6aa09b;
    --pine:#4d7a75;
    --blue:#3d79c2;
    --stone:#a6a39e;
    --charcoal:#6e6a66;
    --silver:#c4c4c4;
    --rule:#b8b8b8;

    --c-protein:var(--mist);
    --c-fitness:var(--blue);
    --c-sports:var(--deep-teal);
    --c-health:var(--slate-teal);
    --c-nutrition:var(--aqua);
    --c-energy:var(--blue);
    --c-supplements:var(--pine);
    --c-accomplished:var(--blue);
  }
  *{margin:0;padding:0;box-sizing:border-box}
  html,body{width:1200px;height:1000px;overflow:hidden}
  body{
    position:relative;
    background:linear-gradient(180deg,#d6d6d6 0%,#f3f3f3 40%,#f6f6f6 60%,#d8d8d8 100%);
    font-family:"Antonio",sans-serif;
  }
  .divider{position:absolute;left:608px;top:55px;width:1px;height:893px;background:var(--rule)}

  .poster{
    position:absolute;width:384px;height:894px;background:#fff;
    box-shadow:4px 6px 14px rgba(0,0,0,.28);
    overflow:hidden;transform-origin:0 0;
  }
  .poster--main{left:133px;top:54px}
  .poster--small{transform:scale(.503)}
  .poster--a{left:697px;top:54px}
  .poster--b{left:908px;top:54px;background:radial-gradient(circle at 30% 20%,#eef3f4 0%,#dbe6e9 45%,#e9eff0 70%,#d4e0e3 100%)}
  .poster--c{left:697px;top:506px;background:#f4f1dc}
  .poster--d{left:908px;top:506px;background:radial-gradient(circle at 60% 40%,#eef0e6 0%,#dfe3d6 50%,#d2d8cc 100%)}
  .poster--small{
    --c-protein:#4e8a8e;--c-fitness:#4e8a8e;--c-sports:#8ec4c6;--c-health:var(--deep-teal);
    --c-nutrition:var(--deep-teal);--c-energy:var(--charcoal);--c-supplements:#2d8aa4;--c-accomplished:#a29e98;
  }

  .open-sign{position:absolute;left:40px;top:40px;width:305px;height:28px;display:flex;align-items:center;justify-content:space-between}
  .open-sign__label{font-family:"Orbitron",sans-serif;font-weight:700;font-size:29px;letter-spacing:6px;margin-right:-6px;color:var(--ink)}
  .chevrons{width:65px;height:24px}

  .word{position:absolute;line-height:1;white-space:nowrap;transform-origin:0 0}
  .sans{font-family:"PT Sans",sans-serif;font-weight:700}
  .tall{font-family:"Six Caps",sans-serif}

  .w-protein{left:41px;top:92px;font-size:47px;color:var(--c-protein)}
  .w-fitness{left:229px;top:97px;font-size:36px;font-weight:600;letter-spacing:3px;color:var(--c-fitness)}
  .w-sports{left:42px;top:140px;font-size:103px;color:var(--c-sports);transform:scaleX(.85)}
  .w-health{left:172px;top:142px;font-size:80px;letter-spacing:14px;color:var(--c-health)}
  .w-creatine{left:40px;top:252px;font-size:40px;font-weight:300;color:var(--stone)}
  .w-science{left:173px;top:226px;font-size:66px;color:var(--slate-teal);transform:scaleX(.91)}
  .w-energy{left:280px;top:231px;font-size:24px;font-weight:600;letter-spacing:1px;color:var(--c-energy)}
  .w-growth{left:280px;top:259px;font-size:24px;font-weight:300;letter-spacing:1px;color:var(--mist)}
  .w-nutrition{left:41px;top:296px;font-size:46px;color:var(--c-nutrition)}
  .w-diet{left:280px;top:299px;font-size:37px;letter-spacing:5px;color:var(--charcoal)}
  .w-weight{left:40px;top:349px;font-size:25px;color:var(--charcoal)}
  .w-loss{left:41px;top:379px;font-size:41px;font-weight:600;color:var(--lagoon)}
  .w-happiness{left:119px;top:342px;font-size:88px;color:var(--deep-teal);transform:scaleX(.79)}
  .w-strong{left:280px;top:350px;font-size:26px;color:var(--sage)}
  .w-natural{left:280px;top:395px;font-size:26px;font-weight:300;letter-spacing:-.5px;color:var(--silver)}
  .w-amino{left:40px;top:438px;font-size:27px;color:#8a8e8e}
  .w-achievement{left:120px;top:436px;font-size:30px;letter-spacing:.5px;color:var(--sage)}
  .w-vitamins{left:281px;top:436px;font-size:30px;letter-spacing:2px;color:var(--slate-teal)}
  .w-performance{left:40px;top:474px;font-size:19.5px;color:var(--deep-teal)}
  .w-testosterone{left:194px;top:478px;font-size:16.5px;letter-spacing:1.2px;color:#4d8f9a}
  .w-organic{left:39px;top:503px;font-size:44px;letter-spacing:1px;color:var(--stone);transform:scaleX(.87)}
  .w-supplements{left:120px;top:504px;font-size:45px;font-weight:700;color:var(--c-supplements)}
  .w-cap-a{left:36px;top:532px;font-size:90px;color:var(--c-accomplished)}
  .w-cap-d{left:296px;top:532px;font-size:90px;color:var(--c-accomplished)}
  .w-vitality{left:123px;top:556px;font-size:32px;letter-spacing:8px;color:var(--deep-teal)}
  .w-accomplished{left:96px;top:591px;font-size:35px;color:var(--c-accomplished)}
  .flag{position:absolute;top:564px;width:22px;height:18px}
  .flag--left{left:92px}
  .flag--right{left:271px}

  .brand{
    position:absolute;left:122px;top:651px;width:141px;height:141px;border-radius:50%;
    border:2px solid var(--ink);display:flex;align-items:center;justify-content:center;text-align:center;
  }
  .brand__name{font-family:"PT Sans",sans-serif;font-weight:700;font-size:19px;line-height:1.15;color:var(--ink)}

  .tagline{
    position:absolute;left:0;top:812px;width:384px;text-align:center;
    font-family:"Orbitron",sans-serif;font-weight:700;font-size:16px;line-height:30px;letter-spacing:4.5px;color:var(--ink);
  }
</style>
</head>
<body>

<div class="divider"></div>

<section class="poster poster--main">
  <div class="open-sign">
    <svg class="chevrons" viewBox="0 0 66 22"><polygon points="12,0 22,0 10,11 22,22 12,22 0,11" fill="#111"/><polygon points="32,0 42,0 30,11 42,22 32,22 20,11" fill="#111"/><polygon points="52,0 62,0 50,11 62,22 52,22 40,11" fill="#111"/></svg>
    <span class="open-sign__label">OPEN</span>
    <svg class="chevrons" viewBox="0 0 66 22"><polygon points="12,0 22,0 10,11 22,22 12,22 0,11" fill="#111"/><polygon points="32,0 42,0 30,11 42,22 32,22 20,11" fill="#111"/><polygon points="52,0 62,0 50,11 62,22 52,22 40,11" fill="#111"/></svg>
  </div>
  <span class="word sans w-protein">PROTEIN</span>
  <span class="word w-fitness">FITNESS</span>
  <span class="word tall w-sports">SPORTS</span>
  <span class="word tall w-health">HEALTH</span>
  <span class="word w-creatine">CREATINE</span>
  <span class="word tall w-science">SCIENCE</span>
  <span class="word w-energy">ENERGY</span>
  <span class="word w-growth">GROWTH</span>
  <span class="word sans w-nutrition">NUTRITION</span>
  <span class="word w-diet">DIET</span>
  <span class="word w-weight">WEIGHT</span>
  <span class="word w-loss">LOSS</span>
  <span class="word tall w-happiness">HAPPINESS</span>
  <span class="word w-strong">STRONG</span>
  <span class="word w-natural">NATURAL</span>
  <span class="word tall w-amino">AMINO ACIDS</span>
  <span class="word w-achievement">ACHIEVEMENT</span>
  <span class="word tall w-vitamins">VITAMINS</span>
  <span class="word sans w-performance">PERFORMANCE</span>
  <span class="word w-testosterone">TESTOSTERONE SUPPORT</span>
  <span class="word tall w-organic">ORGANIC</span>
  <span class="word w-supplements">SUPPLEMENTS</span>
  <span class="word sans w-cap-a">A</span>
  <svg class="flag flag--left" viewBox="0 0 24 18"><polygon points="0,0 24,0 24,18 0,18 8,9" fill="#3aa6ab"/></svg>
  <span class="word w-vitality">VITALITY</span>
  <svg class="flag flag--right" viewBox="0 0 24 18"><polygon points="0,0 24,0 16,9 24,18 0,18" fill="#3aa6ab"/></svg>
  <span class="word sans w-accomplished">CCOMPLISHE</span>
  <span class="word sans w-cap-d">D</span>
  <div class="brand"><span class="brand__name">Harbor<br>Nutrition</span></div>
  <p class="tagline">SUCCESS STARTS<br>HERE.</p>
</section>

<section class="poster poster--small poster--a">
  <div class="open-sign">
    <svg class="chevrons" viewBox="0 0 66 22"><polygon points="12,0 22,0 10,11 22,22 12,22 0,11" fill="#111"/><polygon points="32,0 42,0 30,11 42,22 32,22 20,11" fill="#111"/><polygon points="52,0 62,0 50,11 62,22 52,22 40,11" fill="#111"/></svg>
    <span class="open-sign__label">OPEN</span>
    <svg class="chevrons" viewBox="0 0 66 22"><polygon points="12,0 22,0 10,11 22,22 12,22 0,11" fill="#111"/><polygon points="32,0 42,0 30,11 42,22 32,22 20,11" fill="#111"/><polygon points="52,0 62,0 50,11 62,22 52,22 40,11" fill="#111"/></svg>
  </div>
  <span class="word sans w-protein">PROTEIN</span>
  <span class="word w-fitness">FITNESS</span>
  <span class="word tall w-sports">SPORTS</span>
  <span class="word tall w-health">HEALTH</span>
  <span class="word w-creatine">CREATINE</span>
  <span class="word tall w-science">SCIENCE</span>
  <span class="word w-energy">ENERGY</span>
  <span class="word w-growth">GROWTH</span>
  <span class="word sans w-nutrition">NUTRITION</span>
  <span class="word w-diet">DIET</span>
  <span class="word w-weight">WEIGHT</span>
  <span class="word w-loss">LOSS</span>
  <span class="word tall w-happiness">HAPPINESS</span>
  <span class="word w-strong">STRONG</span>
  <span class="word w-natural">NATURAL</span>
  <span class="word tall w-amino">AMINO ACIDS</span>
  <span class="word w-achievement">ACHIEVEMENT</span>
  <span class="word tall w-vitamins">VITAMINS</span>
  <span class="word sans w-performance">PERFORMANCE</span>
  <span class="word w-testosterone">TESTOSTERONE SUPPORT</span>
  <span class="word tall w-organic">ORGANIC</span>
  <span class="word w-supplements">SUPPLEMENTS</span>
  <span class="word sans w-cap-a">A</span>
  <svg class="flag flag--left" viewBox="0 0 24 18"><polygon points="0,0 24,0 24,18 0,18 8,9" fill="#3aa6ab"/></svg>
  <span class="word w-vitality">VITALITY</span>
  <svg class="flag flag--right" viewBox="0 0 24 18"><polygon points="0,0 24,0 16,9 24,18 0,18" fill="#3aa6ab"/></svg>
  <span class="word sans w-accomplished">CCOMPLISHE</span>
  <span class="word sans w-cap-d">D</span>
  <div class="brand"><span class="brand__name">Harbor<br>Nutrition</span></div>
  <p class="tagline">SUCCESS STARTS<br>HERE.</p>
</section>

<section class="poster poster--small poster--b">
  <div class="open-sign">
    <svg class="chevrons" viewBox="0 0 66 22"><polygon points="12,0 22,0 10,11 22,22 12,22 0,11" fill="#111"/><polygon points="32,0 42,0 30,11 42,22 32,22 20,11" fill="#111"/><polygon points="52,0 62,0 50,11 62,22 52,22 40,11" fill="#111"/></svg>
    <span class="open-sign__label">OPEN</span>
    <svg class="chevrons" viewBox="0 0 66 22"><polygon points="12,0 22,0 10,11 22,22 12,22 0,11" fill="#111"/><polygon points="32,0 42,0 30,11 42,22 32,22 20,11" fill="#111"/><polygon points="52,0 62,0 50,11 62,22 52,22 40,11" fill="#111"/></svg>
  </div>
  <span class="word sans w-protein">PROTEIN</span>
  <span class="word w-fitness">FITNESS</span>
  <span class="word tall w-sports">SPORTS</span>
  <span class="word tall w-health">HEALTH</span>
  <span class="word w-creatine">CREATINE</span>
  <span class="word tall w-science">SCIENCE</span>
  <span class="word w-energy">ENERGY</span>
  <span class="word w-growth">GROWTH</span>
  <span class="word sans w-nutrition">NUTRITION</span>
  <span class="word w-diet">DIET</span>
  <span class="word w-weight">WEIGHT</span>
  <span class="word w-loss">LOSS</span>
  <span class="word tall w-happiness">HAPPINESS</span>
  <span class="word w-strong">STRONG</span>
  <span class="word w-natural">NATURAL</span>
  <span class="word tall w-amino">AMINO ACIDS</span>
  <span class="word w-achievement">ACHIEVEMENT</span>
  <span class="word tall w-vitamins">VITAMINS</span>
  <span class="word sans w-performance">PERFORMANCE</span>
  <span class="word w-testosterone">TESTOSTERONE SUPPORT</span>
  <span class="word tall w-organic">ORGANIC</span>
  <span class="word w-supplements">SUPPLEMENTS</span>
  <span class="word sans w-cap-a">A</span>
  <svg class="flag flag--left" viewBox="0 0 24 18"><polygon points="0,0 24,0 24,18 0,18 8,9" fill="#3aa6ab"/></svg>
  <span class="word w-vitality">VITALITY</span>
  <svg class="flag flag--right" viewBox="0 0 24 18"><polygon points="0,0 24,0 16,9 24,18 0,18" fill="#3aa6ab"/></svg>
  <span class="word sans w-accomplished">CCOMPLISHE</span>
  <span class="word sans w-cap-d">D</span>
  <div class="brand"><span class="brand__name">Harbor<br>Nutrition</span></div>
  <p class="tagline">SUCCESS STARTS<br>HERE.</p>
</section>

<section class="poster poster--small poster--c">
  <div class="open-sign">
    <svg class="chevrons" viewBox="0 0 66 22"><polygon points="12,0 22,0 10,11 22,22 12,22 0,11" fill="#111"/><polygon points="32,0 42,0 30,11 42,22 32,22 20,11" fill="#111"/><polygon points="52,0 62,0 50,11 62,22 52,22 40,11" fill="#111"/></svg>
    <span class="open-sign__label">OPEN</span>
    <svg class="chevrons" viewBox="0 0 66 22"><polygon points="12,0 22,0 10,11 22,22 12,22 0,11" fill="#111"/><polygon points="32,0 42,0 30,11 42,22 32,22 20,11" fill="#111"/><polygon points="52,0 62,0 50,11 62,22 52,22 40,11" fill="#111"/></svg>
  </div>
  <span class="word sans w-protein">PROTEIN</span>
  <span class="word w-fitness">FITNESS</span>
  <span class="word tall w-sports">SPORTS</span>
  <span class="word tall w-health">HEALTH</span>
  <span class="word w-creatine">CREATINE</span>
  <span class="word tall w-science">SCIENCE</span>
  <span class="word w-energy">ENERGY</span>
  <span class="word w-growth">GROWTH</span>
  <span class="word sans w-nutrition">NUTRITION</span>
  <span class="word w-diet">DIET</span>
  <span class="word w-weight">WEIGHT</span>
  <span class="word w-loss">LOSS</span>
  <span class="word tall w-happiness">HAPPINESS</span>
  <span class="word w-strong">STRONG</span>
  <span class="word w-natural">NATURAL</span>
  <span class="word tall w-amino">AMINO ACIDS</span>
  <span class="word w-achievement">ACHIEVEMENT</span>
  <span class="word tall w-vitamins">VITAMINS</span>
  <span class="word sans w-performance">PERFORMANCE</span>
  <span class="word w-testosterone">TESTOSTERONE SUPPORT</span>
  <span class="word tall w-organic">ORGANIC</span>
  <span class="word w-supplements">SUPPLEMENTS</span>
  <span class="word sans w-cap-a">A</span>
  <svg class="flag flag--left" viewBox="0 0 24 18"><polygon points="0,0 24,0 24,18 0,18 8,9" fill="#3aa6ab"/></svg>
  <span class="word w-vitality">VITALITY</span>
  <svg class="flag flag--right" viewBox="0 0 24 18"><polygon points="0,0 24,0 16,9 24,18 0,18" fill="#3aa6ab"/></svg>
  <span class="word sans w-accomplished">CCOMPLISHE</span>
  <span class="word sans w-cap-d">D</span>
  <div class="brand"><span class="brand__name">Harbor<br>Nutrition</span></div>
  <p class="tagline">SUCCESS STARTS<br>HERE.</p>
</section>

<section class="poster poster--small poster--d">
  <div class="open-sign">
    <svg class="chevrons" viewBox="0 0 66 22"><polygon points="12,0 22,0 10,11 22,22 12,22 0,11" fill="#111"/><polygon points="32,0 42,0 30,11 42,22 32,22 20,11" fill="#111"/><polygon points="52,0 62,0 50,11 62,22 52,22 40,11" fill="#111"/></svg>
    <span class="open-sign__label">OPEN</span>
    <svg class="chevrons" viewBox="0 0 66 22"><polygon points="12,0 22,0 10,11 22,22 12,22 0,11" fill="#111"/><polygon points="32,0 42,0 30,11 42,22 32,22 20,11" fill="#111"/><polygon points="52,0 62,0 50,11 62,22 52,22 40,11" fill="#111"/></svg>
  </div>
  <span class="word sans w-protein">PROTEIN</span>
  <span class="word w-fitness">FITNESS</span>
  <span class="word tall w-sports">SPORTS</span>
  <span class="word tall w-health">HEALTH</span>
  <span class="word w-creatine">CREATINE</span>
  <span class="word tall w-science">SCIENCE</span>
  <span class="word w-energy">ENERGY</span>
  <span class="word w-growth">GROWTH</span>
  <span class="word sans w-nutrition">NUTRITION</span>
  <span class="word w-diet">DIET</span>
  <span class="word w-weight">WEIGHT</span>
  <span class="word w-loss">LOSS</span>
  <span class="word tall w-happiness">HAPPINESS</span>
  <span class="word w-strong">STRONG</span>
  <span class="word w-natural">NATURAL</span>
  <span class="word tall w-amino">AMINO ACIDS</span>
  <span class="word w-achievement">ACHIEVEMENT</span>
  <span class="word tall w-vitamins">VITAMINS</span>
  <span class="word sans w-performance">PERFORMANCE</span>
  <span class="word w-testosterone">TESTOSTERONE SUPPORT</span>
  <span class="word tall w-organic">ORGANIC</span>
  <span class="word w-supplements">SUPPLEMENTS</span>
  <span class="word sans w-cap-a">A</span>
  <svg class="flag flag--left" viewBox="0 0 24 18"><polygon points="0,0 24,0 24,18 0,18 8,9" fill="#3aa6ab"/></svg>
  <span class="word w-vitality">VITALITY</span>
  <svg class="flag flag--right" viewBox="0 0 24 18"><polygon points="0,0 24,0 16,9 24,18 0,18" fill="#3aa6ab"/></svg>
  <span class="word sans w-accomplished">CCOMPLISHE</span>
  <span class="word sans w-cap-d">D</span>
  <div class="brand"><span class="brand__name">Harbor<br>Nutrition</span></div>
  <p class="tagline">SUCCESS STARTS<br>HERE.</p>
</section>

</body>
</html>
```